Website for Fashion/Jewelry online seller

We would like a website design that can be used in wordpress. It will be important to be able to link instagram, twitter, etc posts on the bottom of site. We are to be a online seller of chic jewelry, art, fashion, and other home design industries. Currently we emphasize jewelry but as the years move forward, other products will be introduced as collections in home furnishings and primarily women's fashion. It will be important to have a “shop now” section where people can order products online so ecommerce will need to be set up at some point. The website should have the following feel: clean, modern, contemporary and chic. A lot of whites should be used with simple text and simple but elegant fonts. Best is to go to mirevatolkin.example to get the best idea of what we are wanting for the look and feel of the site.

Target Market(s)

upper social class people that are into fashion, jewelry, etc

Industry/Entity Type

Fashion

Number of Pages Required

5+ page

Font styles to use
Other font styles liked:
• go to karodwen.example to see the font desired

Requirements
Must have
• Name of Company is Tide Harbor 7
Nice to have
• see project description
Should not have
• see project description

```html
<!DOCTYPE html>
<html lang="en">
<head>
<meta charset="utf-8">
<title>Tide Harbor 7 — Jewellery</title>
<link rel="stylesheet" href="https://fonts.googleapis.com/css2?family=Bodoni+Moda:wght@400;500&family=Open+Sans:ital,wght@0,400;0,600;0,700;1,400;1,600&display=swap">
<style>
:root{
  --page:#f4f4f4;
  --band:#f9f9f9;
  --section:#f0f0f0;
  --white:#ffffff;
  --ink:#333333;
  --heading:#3a3a3a;
  --muted:#9a9a9a;
  --nav:#8a8a8a;
  --accent:#7a4f8c;
  --footer:#2b2829;
  --line:#d8d8d8;
}
*{box-sizing:border-box;margin:0;padding:0}
html,body{width:1200px;height:2620px;overflow:hidden}
body{position:relative;background:var(--page);font-family:"Open Sans",Arial,sans-serif;color:var(--ink)}
.abs{position:absolute}
.serif{font-family:"Bodoni Moda","Times New Roman",serif}

/* header */
.site-header{left:0;top:0;width:1200px;height:108px;background:#f5f5f5;box-shadow:0 3px 6px rgba(0,0,0,.18)}
.nav-divider{left:664px;top:30px;width:1px;height:52px;background:var(--line)}
.nav-item{top:46px;font-size:13px;font-weight:700;letter-spacing:.5px;color:var(--nav)}
.nav-item.is-active{color:#222}
.cart-total{left:959px;top:112px;width:154px;height:28px;background:var(--white);box-shadow:0 2px 4px rgba(0,0,0,.2);font-size:14px;font-weight:700;color:#777;display:flex;align-items:center;justify-content:center;gap:8px}

/* hero */
.hero{left:89px;top:175px;width:870px;height:379px;background:linear-gradient(100deg,#8a6f60 0%,#c9a894 30%,#b79a7d 55%,#6f5b4c 80%,#9b8a78 100%)}
.hero-thumb{left:959px;width:154px;height:126px}
.price-tag{left:89px;top:227px;height:32px;width:132px;background:var(--white);clip-path:polygon(0 0,88% 0,100% 50%,88% 100%,0 100%);font-size:20px;font-weight:700;color:#444;padding-left:16px;line-height:32px}
.price-tag small{font-size:13px}
.cart-tag{left:89px;top:271px;height:31px;width:81px;background:var(--white);clip-path:polygon(0 0,80% 0,100% 50%,80% 100%,0 100%);padding:7px 0 0 18px}
.hero-caption{left:89px;top:428px;width:870px;height:96px;background:rgba(190,165,150,.55);border-top:2px solid var(--white);border-bottom:2px solid var(--white);padding:8px 0 0 68px}
.hero-caption h2{font-size:24px;font-weight:400;color:#5a4a44}
.hero-caption p{font-size:14px;font-style:italic;color:#fff;line-height:20px;width:640px;margin-top:2px}

/* tagline */
.tagline-band{left:0;top:615px;width:1200px;height:115px;background:var(--band);display:flex;align-items:center;justify-content:center}
.tagline-band p{font-size:31px;color:#555}

/* products */
.products{left:0;top:730px;width:1200px;height:310px;background:var(--section)}
.product-card{top:797px;width:240px;height:178px;background:var(--white)}
.product-image{width:240px;height:129px}
.product-label{position:absolute;left:0;top:129px;width:240px;height:49px;text-align:center;padding-top:8px;font-size:17px;color:#777}

/* articles */
.articles{left:0;top:1040px;width:1200px;height:553px;background:var(--band)}
.feature-image{left:89px;top:1067px;width:501px;height:327px;background:linear-gradient(135deg,#e8e4e2 0%,#d9c7b8 45%,#2a2c3a 75%,#3b3b48 100%)}
.feature-title{left:89px;top:1424px;font-size:24px;color:#222}
.feature-text{left:89px;top:1467px;width:501px;font-size:12.5px;line-height:18.5px;color:var(--muted)}
.more{font-size:13px;font-style:italic;font-weight:600;color:var(--accent)}
.article-thumb{left:611px;width:152px;height:152px}
.article-title{left:788px;font-size:21px;color:#333}
.article-text{left:788px;width:325px;font-size:12.5px;line-height:18.5px;color:var(--muted)}
.article-text.is-lead{font-weight:700;font-size:13.5px;line-height:20px}

/* gallery */
.gallery{left:0;top:1593px;width:1200px;height:640px;background:var(--section)}
.gallery-image{top:1710px;width:330px;height:400px;border:1px solid #ddd}

/* footer */
.site-footer{left:0;top:2233px;width:1200px;height:387px;background:var(--footer);color:var(--white)}
.footer-heading{top:2290px;font-size:23px;font-weight:400;letter-spacing:.5px}
.footer-links{top:2328px;list-style:none;font-size:11px;line-height:22px;letter-spacing:.2px}
.field{left:807px;width:297px;background:var(--white);font-size:11px;color:#888;padding:10px 18px;letter-spacing:.5px}
.send-btn{left:807px;top:2512px;width:152px;height:35px;background:var(--white);color:#333;font-size:11.5px;letter-spacing:.8px;display:flex;align-items:center;justify-content:center}
.copyright{left:79px;top:2564px;font-size:21px;letter-spacing:.5px}
</style>
</head>
<body>

<header class="site-header abs" aria-label="Tide Harbor 7">
</header>
<div class="nav-divider abs"></div>
<nav>
  <span class="nav-item is-active abs" style="left:692px">SHOP</span>
  <span class="nav-item abs" style="left:779px">ABOUT</span>
  <span class="nav-item abs" style="left:864px">CHARITY</span>
  <span class="nav-item abs" style="left:947px">LOCATIONS</span>
  <span class="nav-item abs" style="left:1046px">CONTACT</span>
</nav>
<div class="cart-total abs">
  <svg width="18" height="14" viewBox="0 0 18 14" aria-hidden="true"><path d="M1 1h3l2 8h9l2-6H5" fill="none" stroke="#777" stroke-width="1.6"/><circle cx="7" cy="12" r="1.4" fill="#777"/><circle cx="14" cy="12" r="1.4" fill="#777"/></svg>
  <span>TOTAL:</span><span style="margin-left:14px">$499</span>
</div>

<section>
  <div class="hero abs" role="img" aria-label="Model wearing a long pearl necklace in front of arched terrace"></div>
  <div class="hero-thumb abs" style="top:175px;background:linear-gradient(160deg,#b63a3a,#d9a36a,#7a2a2a)" role="img" aria-label="Bride in traditional gold jewellery"></div>
  <div class="hero-thumb abs" style="top:301px;background:linear-gradient(160deg,#6b7a4a,#c9c2b4,#59603e)" role="img" aria-label="Hands wearing rings"></div>
  <div class="hero-thumb abs" style="top:427px;background:linear-gradient(160deg,#5f7a4f,#b89b84,#3f5a3a)" role="img" aria-label="Turquoise ring beside a cactus"></div>
  <div class="price-tag abs">$499,<small>00</small></div>
  <div class="cart-tag abs"><svg width="26" height="18" viewBox="0 0 18 14" aria-label="Add to cart"><path d="M1 1h3l2 8h9l2-6H5" fill="none" stroke="#888" stroke-width="1.5"/><circle cx="7" cy="12" r="1.4" fill="#888"/><circle cx="14" cy="12" r="1.4" fill="#888"/></svg></div>
  <div class="hero-caption abs">
    <h2 class="serif">Lorem Ipsum Jewellery</h2>
    <p>Lorem ipsum dolor sit amet, consectetur adipiscing elit. Proin quam libero, pellentesque eget tellus vel, dapibus interdum leo. Mauris sollicitudin augue at dignissim vulputate.</p>
  </div>
</section>

<section class="tagline-band abs">
  <p class="serif">We fancy ourselves to be a One Stop Jewellery Shop</p>
</section>

<section class="products abs"></section>
<div class="product-card abs" style="left:87px"><div class="product-image" style="background:linear-gradient(135deg,#2a8fb0,#5ab8cf,#c9b08a)" role="img" aria-label="Turquoise wrap bracelet"></div><div class="product-label serif">Lorem Ipsum</div></div>
<div class="product-card abs" style="left:348px"><div class="product-image" style="background:linear-gradient(135deg,#5a5a66,#8a8790,#c9b79a)" role="img" aria-label="Grey leather bracelet with silver charms"></div><div class="product-label serif">Lorem Ipsum</div></div>
<div class="product-card abs" style="left:610px"><div class="product-image" style="background:linear-gradient(135deg,#6b3a22,#3aa0b5,#5a3220)" role="img" aria-label="Turquoise bead necklace on wooden plate"></div><div class="product-label serif">Lorem Ipsum</div></div>
<div class="product-card abs" style="left:872px"><div class="product-image" style="background:linear-gradient(135deg,#c9b79a,#5c5c6a,#c9b79a)" role="img" aria-label="Braided grey bracelet with gold beads"></div><div class="product-label serif">Lorem Ipsum</div></div>

<section class="articles abs"></section>
<div class="feature-image abs" role="img" aria-label="Woman seated on an antique iron bed"></div>
<h3 class="feature-title abs serif" style="font-weight:400">Lorem ipsum dolor sit amet,</h3>
<p class="feature-text abs">Proin gravida nibh vel velit auctor aliquet. Aenean sollicitudin, lorem quis bibendum auctor, nisi elit consequat ipsum, nec sagittis sem nibh id elit. Proin gravida nibh vel velit auctor aliquet. Aenean sollicitudin, lorem quis bibendum auctor.</p>
<span class="more abs" style="left:466px;top:1545px">Continue reading...</span>

<div class="article-thumb abs" style="top:1067px;background:linear-gradient(135deg,#c9a0a0,#e8e0dc,#3a3434)" role="img" aria-label="Couple shopping for jewellery"></div>
<h4 class="article-title abs serif" style="top:1060px;font-weight:400">Lorem ipsum</h4>
<p class="article-text is-lead abs" style="top:1106px">Proin gravida nibh vel velit auctor aliquet. Aenean sollicitudin, lorem quis bibendum auctor, nisi elit consequat</p>
<span class="more abs" style="left:990px;top:1185px">Continue reading...</span>

<div class="article-thumb abs" style="top:1242px;background:linear-gradient(135deg,#e9e4df,#d9b99a,#8a8a8a)" role="img" aria-label="Smiling couple admiring a ring"></div>
<h4 class="article-title abs serif" style="top:1235px;font-weight:400">Lorem Ipsum</h4>
<p class="article-text abs" style="top:1282px">Proin gravida nibh vel velit auctor aliquet. Aenean sollicitudin, lorem quis bibendum auctor, nisi elit consequat ipsum, nec sagittis sem nibh id elit.</p>
<span class="more abs" style="left:990px;top:1359px">Continue reading...</span>

<div class="article-thumb abs" style="top:1417px;background:linear-gradient(135deg,#3a2a22,#9a7a66,#2a2a30)" role="img" aria-label="Smiling woman in a denim jacket"></div>
<h4 class="article-title abs serif" style="top:1410px;font-weight:400">Lorem Ipsum</h4>
<p class="article-text abs" style="top:1457px">Proin gravida nibh vel velit auctor aliquet. Aenean sollicitudin, lorem quis bibendum auctor, nisi elit consequat ipsum, nec sagittis sem nibh id elit.</p>
<span class="more abs" style="left:990px;top:1545px">Continue reading...</span>

<section class="gallery abs"></section>
<div class="gallery-image abs" style="left:82px;background:linear-gradient(160deg,#2a2a2a,#d9bf96,#e8d6b4,#3a4a8a)" role="img" aria-label="Woman in embroidered cream saree at an event"></div>
<div class="gallery-image abs" style="left:433px;background:linear-gradient(160deg,#e8ecef,#b5a89a,#6c7a8a,#d9d9d9)" role="img" aria-label="Two women laughing at a jewellery counter"></div>
<div class="gallery-image abs" style="left:784px;background:linear-gradient(180deg,#0f1a3a,#1a2f5a,#2a5a8a,#b5c4d6)" role="img" aria-label="Woman in black gown on a balcony above a city at night"></div>

<footer class="site-footer abs"></footer>
<h5 class="footer-heading abs serif" style="left:154px;color:#fff">LOREM IPSUM</h5>
<ul class="footer-links abs" style="left:150px;color:#fff"><li>LOREM IPSUM</li><li>LOREM IPSUM LOREM</li><li>LOREM IPSUM</li><li>LOREM IPSUM</li><li>LOREM</li></ul>
<h5 class="footer-heading abs serif" style="left:480px;color:#fff">LOREM IPSUM</h5>
<ul class="footer-links abs" style="left:480px;color:#fff"><li>LOREM IPSUM</li><li>LOREM IPSUM LOREM</li><li>LOREM IPSUM</li><li>LOREM IPSUM</li><li>LOREM</li></ul>
<h5 class="footer-heading abs serif" style="left:807px;color:#fff">CONTACT US</h5>
<div class="field abs" style="top:2339px;height:37px">YOUR E-MAIL...</div>
<div class="field abs" style="top:2399px;height:89px">YOUR TEXT...</div>
<div class="send-btn abs">SEND MESSAGE</div>
<p class="copyright abs serif" style="color:#fff">COPY RIGHTS @ 2016 : ALL RIGHTS RESERVED</p>

</body>
</html>
```